Nutrition product information web site

Nutrition Website (see upload) without Shop function but link to Velmora ASIN number that customer could order from Velmora direct. Content must be easily editable without coding. Web environment must be responsive to support mobile devices as well. design should be modern and clear. loading of web elements must be fast. not too much time consuming features.

Industry/Entity Type

Nutrition

Number of Pages Required

5+ page

Font styles to use
Sans Serif

Colors
33b8a4
9bcb3c
0255a3
0a90cc
a54499

Requirements
Must have
• read attached document
Nice to have
• read attached document
Should not have
• read attached document

```html
<!DOCTYPE html>
<html lang="en">
<head>
<meta charset="utf-8">
<title>Nuvara – Well Being Through Smart Research</title>
<link href="https://fonts.googleapis.com/css2?family=Montserrat:wght@400;500;600;700&display=swap" rel="stylesheet">
<style>
:root{
  --teal:#2bbcc4;
  --ink:#2d2d2d;
  --muted:#8a8f93;
  --band:#e8f0ef;
  --nav:#eef4f4;
  --hero-top:#3d5965;
  --hero-bottom:#4a6470;
  --white:#ffffff;
}
*{margin:0;padding:0;box-sizing:border-box}
html,body{width:1200px;height:1200px;overflow:hidden;background:var(--white)}
body{font-family:'Montserrat',sans-serif;color:var(--ink);position:relative}
.page{position:absolute;left:320px;top:0;width:701px;height:1500px;transform:scale(0.8);transform-origin:0 0}
.abs{position:absolute}
.nav{left:0;top:0;width:701px;height:27px;background:var(--nav);box-shadow:0 1px 3px rgba(0,0,0,.12)}
.brand-mini{left:123px;top:3px;width:49px;height:11px;background:var(--ink);color:var(--white);font-size:8px;font-weight:700;letter-spacing:1px;text-align:center;line-height:11px}
.nav-link{top:6px;font-size:6px;color:var(--muted);letter-spacing:.3px}
.nav-link.active{color:var(--teal)}
.hero{left:0;top:27px;width:701px;height:222px;background:linear-gradient(180deg,var(--hero-top),var(--hero-bottom))}
.hero-title{left:0;top:124px;width:701px;text-align:center;color:var(--white);font-size:14px;font-weight:500}
.hero-title span{color:var(--teal);font-weight:600}
.hero-sub{left:0;top:142px;width:701px;text-align:center;color:var(--white);font-size:6.5px;font-weight:600}
.section-title{font-size:18px;color:var(--teal);font-weight:400}
.body-text{font-size:5px;line-height:11px;color:var(--muted)}
.btn{background:var(--teal);color:var(--white);font-size:6px;font-weight:700;text-align:center}
.brand-name{font-size:15px;font-weight:700;letter-spacing:2px;color:var(--ink)}
.band{left:0;top:522px;width:701px;height:164px;background:var(--band)}
.bottle{border-radius:6px;background:linear-gradient(90deg,#dfe3e5,#ffffff 45%,#e3e6e8)}
.cap{font-size:5px;color:var(--ink);text-align:center;width:80px}
.price{font-size:6px;color:var(--teal);text-align:center;width:80px}
.arrow-txt{font-size:6.5px;color:var(--muted);border-bottom:1px solid #c9cfd0;padding-bottom:1px}
.card{left:274px;top:486px;width:152px;height:239px;background:var(--white);box-shadow:0 2px 8px rgba(0,0,0,.18)}
.num{width:18px;height:18px;border-radius:50%;background:var(--teal);color:var(--white);font-size:8px;font-weight:600;text-align:center;line-height:18px}
.feat-title{font-size:8.5px;color:var(--ink)}
.feat-text{font-size:4.5px;color:var(--muted)}
.photo{top:1074px;width:105px;height:94px}
.blog-cap{top:1176px;width:105px;text-align:center;font-size:5px;color:var(--ink);line-height:7px}
.blog-date{top:1192px;width:105px;text-align:center;font-size:4px;color:var(--muted)}
.map{left:0;top:1231px;width:701px;height:159px;background:linear-gradient(135deg,#c6c9ca,#dcdedf 50%,#c9cccd)}
.foot-head{font-size:7.5px;font-weight:600;color:var(--ink);letter-spacing:.5px}
.foot-item{font-size:4.5px;color:var(--ink)}
</style>
</head>
<body>
<div class="page">
  <header class="nav abs">
    <div class="brand-mini abs">NUVARA</div>
    <span class="nav-link active abs" style="left:228px">HOME</span>
    <span class="nav-link abs" style="left:274px">ABOUT</span>
    <span class="nav-link abs" style="left:323px">PRODUCT</span>
    <span class="nav-link abs" style="left:386px">BLOG</span>
    <span class="nav-link abs" style="left:434px">CONTACT</span>
    <svg class="abs" style="left:490px;top:6px" width="50" height="9" viewBox="0 0 50 9" fill="none" stroke="#2bbcc4" stroke-width="1">
      <circle cx="4" cy="4" r="2.5"/><line x1="6" y1="6" x2="8" y2="8"/>
      <circle cx="23" cy="3" r="1.8"/><path d="M20 8q3-4 6 0"/>
      <rect x="39" y="2" width="4" height="6"/>
    </svg>
    <span class="nav-link abs" style="left:556px">Eng</span>
    <svg class="abs" style="left:571px;top:7px" width="6" height="5"><path d="M0 0h6L3 5z" fill="#2bbcc4"/></svg>
  </header>

  <section class="hero abs" role="img" aria-label="Person meditating on a misty shore at dusk"></section>
  <h1 class="hero-title abs">WELL BEING <span>THROUGH SMART</span> RESEARCH</h1>
  <p class="hero-sub abs">Balance your life &amp; nourish your soul</p>
  <svg class="abs" style="left:330px;top:236px" width="40" height="33" viewBox="0 0 40 33">
    <path d="M0 13h40L20 33z" fill="#4a6470"/>
    <circle cx="20" cy="13" r="9" fill="#4a6470" stroke="#fff" stroke-width="1.5"/>
    <path d="M16.5 10.5h7L20 16z" fill="#2bbcc4"/>
  </svg>

  <h2 class="section-title abs" style="left:124px;top:299px">ABOUT US</h2>
  <p class="body-text abs" style="left:123px;top:338px;width:272px">Lorem ipsum dolor sit amet, consectetur adipiscing elit. Donec facilisis enim sed ipsum posuere, vel facilisis tortor rhoncus. Duis tempor rutrum ante. Nullam scelerisque mi quis condimentum ullamcorper. Lorem ipsum dolor sit amet, consectetur adipiscing elit. Donec facilisis enim sed ipsum posuere, vel facilisis tortor rhoncus. Duis tempor rutrum ante. Nullam scelerisque mi quis condimentum ullamcorper.</p>
  <div class="btn abs" style="left:123px;top:393px;width:67px;height:18px;line-height:18px">MORE</div>
  <svg class="abs" style="left:524px;top:320px" width="28" height="28"><circle cx="14" cy="14" r="12.5" fill="none" stroke="#2bbcc4" stroke-width="2"/></svg>
  <div class="brand-name abs" style="left:497px;top:351px">NUVARA</div>

  <div class="band abs"></div>
  <span class="arrow-txt abs" style="left:90px;top:587px">prew</span>
  <span class="arrow-txt abs" style="left:590px;top:587px">next</span>

  <div class="bottle abs" style="left:136px;top:554px;width:40px;height:70px" role="img" aria-label="Sorell Focus herbal supplement jar"></div>
  <div class="cap abs" style="left:116px;top:629px">LOREM IPSUM DOLOR</div>
  <div class="price abs" style="left:116px;top:636px">$120</div>
  <div class="bottle abs" style="left:213px;top:554px;width:40px;height:70px" role="img" aria-label="Tavine Calm mood supplement jar"></div>
  <div class="cap abs" style="left:193px;top:629px">LOREM IPSUM DOLOR</div>
  <div class="price abs" style="left:193px;top:636px">$120</div>
  <div class="bottle abs" style="left:447px;top:554px;width:40px;height:70px" role="img" aria-label="Sorell Focus herbal supplement jar"></div>
  <div class="cap abs" style="left:427px;top:629px">LOREM IPSUM DOLOR</div>
  <div class="price abs" style="left:427px;top:636px">$120</div>
  <div class="bottle abs" style="left:524px;top:554px;width:40px;height:70px" role="img" aria-label="Tavine Calm mood supplement jar"></div>
  <div class="cap abs" style="left:504px;top:629px">LOREM IPSUM DOLOR</div>
  <div class="price abs" style="left:504px;top:636px">$120</div>

  <div class="card abs"></div>
  <div class="bottle abs" style="left:307px;top:502px;width:86px;height:139px" role="img" aria-label="Orbena Daily vitamin supplement jar, 60 capsules"></div>
  <div class="abs" style="left:274px;top:649px;width:152px;text-align:center;font-size:6px">LOREM IPSUM DOLOR SIT AMET</div>
  <div class="abs" style="left:274px;top:659px;width:152px;text-align:center;font-size:6px;color:var(--teal);letter-spacing:2px">★★★★<span style="color:#ccc">★</span></div>
  <div class="abs" style="left:274px;top:670px;width:152px;text-align:center;font-size:10px;font-weight:700">$ 127</div>
  <div class="btn abs" style="left:299px;top:694px;width:105px;height:20px;line-height:20px;font-weight:500">
    <svg width="8" height="7" style="vertical-align:-1px;margin-right:5px" viewBox="0 0 8 7" fill="none" stroke="#fff"><path d="M0 .5h1.5l1 4h4l1-3H2"/><circle cx="3" cy="6" r=".5"/><circle cx="6" cy="6" r=".5"/></svg>www.velmora.com
  </div>

  <h2 class="abs" style="left:0;top:766px;width:701px;text-align:center;font-size:17px;font-weight:400"><span style="color:var(--teal)">WHY</span> NUVARA</h2>
  <p class="body-text abs" style="left:160px;top:799px;width:381px;text-align:center">Lorem ipsum dolor sit amet, consectetur adipiscing elit. Donec facilisis enim sed ipsum posuere, vel facilisis tortor rhoncus. Duis tempor rutrum ante. Nullam scelerisque mi quis condimentum ullamcorper. Lorem ipsum dolor sit amet, consectetur adipiscing elit. Donec facilisis enim sed ipsum posuere, vel facilisis tortor rhoncus. Duis tempor rutrum ante. Nullam scelerisque mi quis condimentum ullamcorper.</p>

  <div class="num abs" style="left:162px;top:877px">1</div>
  <div class="feat-title abs" style="left:187px;top:876px">EASY TO USE</div>
  <div class="feat-text abs" style="left:187px;top:889px">Lorem ipsum dolor sit amet, consectetur adipiscing elit. Donec facilisis enim sed.</div>
  <div class="num abs" style="left:162px;top:912px">2</div>
  <div class="feat-title abs" style="left:186px;top:911px">SHOP WORLD BEST ONLIE STORE</div>
  <div class="feat-text abs" style="left:187px;top:924px">Lorem ipsum dolor <span style="color:var(--teal)">www.velmora.com</span> adipiscing elit. Donec facilisis enim sed.</div>
  <div class="num abs" style="left:162px;top:951px">3</div>
  <div class="feat-title abs" style="left:187px;top:949px">NO SIDE EFFECTS</div>
  <div class="feat-text abs" style="left:187px;top:962px">Lorem ipsum dolor sit amet, consectetur adipiscing elit. Donec facilisis enim sed.</div>

  <div class="bottle abs" style="left:480px;top:866px;width:56px;height:96px" role="img" aria-label="Tavine Calm mood supplement jar"></div>
  <div class="abs" style="left:446px;top:969px;width:120px;text-align:center;font-size:7px">LOREM IPSUM DOLOR</div>
  <div class="abs" style="left:446px;top:981px;width:120px;text-align:center;font-size:7.5px;color:var(--teal)">$120</div>
  <svg class="abs" style="left:492px;top:1000px" width="30" height="6"><circle cx="3" cy="3" r="2" fill="#ccc"/><circle cx="14" cy="3" r="2" fill="#2bbcc4"/><circle cx="26" cy="3" r="2" fill="#ccc"/></svg>

  <h2 class="section-title abs" style="left:0;top:1042px;width:701px;text-align:center">BLOG</h2>
  <span class="arrow-txt abs" style="left:91px;top:1120px">prew</span>
  <span class="arrow-txt abs" style="left:590px;top:1120px">next</span>
  <div class="photo abs" style="left:123px;background:linear-gradient(135deg,#4c5a3a,#8fae55 50%,#c9c6a5)" role="img" aria-label="Bowl of fresh green salad"></div>
  <div class="photo abs" style="left:239px;background:linear-gradient(180deg,#6c8fb8,#c9d8e8 60%,#e4e7ea)" role="img" aria-label="Man with open arms under a bright sky"></div>
  <div class="photo abs" style="left:356px;background:linear-gradient(135deg,#5b3a26,#8a5a38 50%,#b23a3a)" role="img" aria-label="Salad plate and wooden spoons on a table"></div>
  <div class="photo abs" style="left:473px;background:linear-gradient(135deg,#6fa24a,#e887a8 55%,#d9464f)" role="img" aria-label="Child eating a slice of watermelon"></div>
  <div class="blog-cap abs" style="left:123px">LOREM IPSUM DOLOR SIT AMET<br>CONSECTETUR</div>
  <div class="blog-cap abs" style="left:239px">LOREM IPSUM DOLOR SIT AMET<br>CONSECTETUR</div>
  <div class="blog-cap abs" style="left:356px">LOREM IPSUM DOLOR SIT AMET<br>CONSECTETUR</div>
  <div class="blog-cap abs" style="left:473px">LOREM IPSUM DOLOR SIT AMET<br>CONSECTETUR</div>
  <div class="blog-date abs" style="left:123px">Aug 15, 2018</div>
  <div class="blog-date abs" style="left:239px">Aug 15, 2018</div>
  <div class="blog-date abs" style="left:356px">Aug 15, 2018</div>
  <div class="blog-date abs" style="left:473px">Aug 15, 2018</div>

  <div class="map abs" role="img" aria-label="Map of store locations in the region"></div>

  <svg class="abs" style="left:147px;top:1412px" width="30" height="30"><circle cx="15" cy="15" r="13.5" fill="none" stroke="#2bbcc4" stroke-width="2"/></svg>
  <div class="brand-name abs" style="left:121px;top:1443px">NUVARA</div>
  <div class="abs" style="left:123px;top:1469px;font-size:6px">Get Social</div>
  <svg class="abs" style="left:168px;top:1469px" width="34" height="8" fill="none" stroke="#2bbcc4" stroke-width=".8">
    <circle cx="4" cy="4" r="3.3"/><circle cx="16" cy="4" r="3.3"/><circle cx="28" cy="4" r="3.3"/>
  </svg>

  <div class="foot-head abs" style="left:317px;top:1418px">CONTACT</div>
  <svg class="abs" style="left:316px;top:1446px" width="6" height="32" fill="none" stroke="#2bbcc4" stroke-width=".7">
    <rect x="1" y="0" width="4" height="6" rx=".6"/>
    <rect x=".5" y="13" width="5" height="3.5"/><path d="M.5 13l2.5 2 2.5-2"/>
    <path d="M3 31c-2-2.5-2.5-3.5-2.5-4.5a2.5 2.5 0 015 0c0 1-.5 2-2.5 4.5z"/>
  </svg>
  <div class="foot-item abs" style="left:328px;top:1447px">+91 0000 555 123</div>
  <div class="foot-item abs" style="left:328px;top:1459px">hello@nuvara.example</div>
  <div class="foot-item abs" style="left:328px;top:1471px">12/4, LAKE CITY</div>

  <div class="foot-head abs" style="left:434px;top:1418px">GET A NWESLETTER</div>
  <p class="abs" style="left:433px;top:1446px;width:102px;font-size:4px;line-height:8px;color:var(--muted)">Lorem ipsum dolor sit amet, consectetur adipisc ing elit. Donec enim augue vitae dui consectetur</p>
  <div class="abs" style="left:433px;top:1468px;width:84px;font-size:4.5px;border-bottom:1px solid #ccc;padding-bottom:2px">Enter Your e-mail</div>
  <svg class="abs" style="left:515px;top:1469px" width="16" height="16"><circle cx="8" cy="8" r="7.5" fill="#2bbcc4"/><path d="M4 8l8-3-3 8-1-4z" fill="#fff"/></svg>
</div>
</body>
</html>
```